Vek furniture

A single page e commerce website for a new furniture company.

The opening range would consist of 3 collections - Each collection would consist of a bed , sofa & arm chair.

So total 9 items.

We would want a single page which has the 3 collections on it which are available to purchase from the website.

See attached the logo & branding for colours

Target Market(s)

customers wanting to buy high end furniture

Industry/Entity Type

furniture retail

Coding

Coded - Design and coding required

Number of Pages Required

1 page

Colors
00AB8E
00BBA5
67D7C9
C6EFE9
E9F9F6

```html
<!DOCTYPE html>
<html lang="en">
<head>
<meta charset="utf-8">
<title>Vek furniture</title>
<link rel="stylesheet" href="https://fonts.googleapis.com/css2?family=Montserrat:wght@400;500;600;700;800&family=Poppins:wght@400;500;600&display=swap">
<style>
:root{
  --brand:#0BA7AE;
  --teal:#00AB8E;
  --teal-2:#00BBA5;
  --mint:#67D7C9;
  --mint-soft:#C6EFE9;
  --mint-pale:#E9F9F6;
  --ink:#2a2a2a;
  --text:#4a4a4a;
  --white:#fff;
  --black:#000;
  --star:#f5b301;
}
*{box-sizing:border-box;margin:0;padding:0}
html,body{width:1200px;height:4089px;overflow:hidden}
body{font-family:'Poppins',sans-serif;color:var(--text);background:var(--white);position:relative}
a{color:inherit}

/* header */
.site-header{position:absolute;left:0;top:0;width:1200px;height:111px;background:var(--brand)}
.brand-name{position:absolute;left:113px;top:38px;font-family:'Montserrat',sans-serif;font-weight:600;font-size:28px;line-height:34px;color:var(--white);letter-spacing:1px}
.main-nav{position:absolute;top:48px;left:440px;display:flex;gap:37px;font-family:'Montserrat',sans-serif;font-weight:600;font-size:14px;color:var(--white)}
.nav-icons{position:absolute;top:44px;left:978px;display:flex;gap:18px}

/* hero */
.hero{position:absolute;left:0;top:111px;width:1200px;height:616px;background:var(--mint);overflow:hidden}
.hero .big{position:absolute;left:104px;top:140px;font-family:'Montserrat',sans-serif;font-weight:600;font-size:232px;line-height:1;color:#eafaf7;letter-spacing:20px}
.hero .kicker{position:absolute;left:108px;top:332px;font-family:'Montserrat',sans-serif;font-weight:500;font-size:22px;letter-spacing:3px;color:var(--white)}
.hero h1{position:absolute;left:106px;top:358px;font-family:'Montserrat',sans-serif;font-weight:600;font-size:88px;letter-spacing:9px;color:var(--white);line-height:1.1}
.hero-photo{position:absolute;left:488px;top:64px;width:600px;height:560px;border-radius:90px 90px 40px 40px;background:radial-gradient(ellipse at 50% 40%,#5a7fc4,#3a5c9e 70%)}
.hero-bump{position:absolute;left:526px;top:588px;width:148px;height:74px;border-radius:74px 74px 0 0;background:var(--white)}

.btn{display:flex;align-items:center;justify-content:center;font-family:'Poppins',sans-serif;font-weight:500;font-size:14px;color:var(--white);background:var(--teal);border:2px solid var(--white);outline:2px solid var(--teal);position:absolute;text-decoration:none}
.btn::after{content:"";position:absolute;right:-8px;top:50%;width:14px;height:14px;margin-top:-7px;border-radius:50%;background:var(--white)}

.dots{position:absolute;display:flex;align-items:center;gap:12px}
.dots i{display:block;width:10px;height:10px;border-radius:50%;background:var(--brand)}
.dots i.on{width:18px;height:18px;border:2px solid var(--brand);background:transparent;position:relative}
.dots i.on::after{content:"";position:absolute;inset:3px;border-radius:50%;background:var(--brand)}

/* category */
.section-ghost{position:absolute;left:0;width:1200px;text-align:center;font-family:'Montserrat',sans-serif;font-weight:800;color:#e3e3e3;letter-spacing:8px}
.section-title{position:absolute;left:0;width:1200px;text-align:center;font-family:'Montserrat',sans-serif;font-weight:700;color:var(--brand);letter-spacing:5px}
.cat{position:absolute;width:294px;height:357px}
.cat .frame{position:absolute;left:6px;top:-6px;width:294px;height:357px;border:2px solid var(--brand)}
.cat .card{position:absolute;inset:0;background:var(--brand);text-align:center}
.cat.alt .card{background:var(--teal-2)}
.cat.alt .frame{border-color:var(--teal-2)}
.cat .notch{position:absolute;left:122px;top:-24px;width:50px;height:50px;border-radius:50%;background:var(--white)}
.cat h3{margin-top:52px;font-family:'Montserrat',sans-serif;font-weight:800;font-size:34px;letter-spacing:3px;color:var(--white)}
.cat a{display:block;margin-top:6px;font-size:15px;color:var(--white);text-decoration:underline}
.cat .pic{position:absolute;border-radius:14px}

/* products */
.products{position:absolute;left:0;top:1519px;width:1200px;height:1028px;background:var(--mint-pale)}
.products h2{position:absolute;left:0;top:64px;width:1200px;text-align:center;font-family:'Montserrat',sans-serif;font-weight:700;font-size:52px;color:var(--ink)}
.products .rule{position:absolute;left:564px;top:138px;width:72px;height:4px;background:var(--ink)}
.tab{position:absolute;top:165px;height:60px;display:flex;align-items:center;justify-content:center;gap:34px;font-family:'Montserrat',sans-serif;font-weight:500;font-size:22px;letter-spacing:3px;color:var(--brand);background:#b5e5e6}
.tab.on{background:var(--brand);color:var(--white)}
.prod{position:absolute;top:274px;width:300px;height:580px;text-align:center}
.prod .box{height:361px;background:var(--white);border:8px solid #f3f3f3;box-shadow:0 2px 8px rgba(0,0,0,.12);position:relative}
.prod .pic{position:absolute;left:38px;top:48px;width:208px;height:224px;border-radius:60px 60px 20px 20px}
.prod .stars{position:absolute;left:0;bottom:10px;width:100%;color:var(--star);font-size:16px;letter-spacing:2px}
.prod .price{margin-top:30px;font-size:17px;line-height:24px;font-weight:500;color:var(--ink)}
.prod h4{margin-top:8px;font-family:'Montserrat',sans-serif;font-weight:600;font-size:20px;line-height:26px;color:var(--ink);letter-spacing:.5px}
.prod p{margin:8px -10px 0;font-size:13px;line-height:21px;color:#555}
.prod .btn{left:78px;top:517px;width:144px;height:47px}

/* news */
.news-title{position:absolute;left:107px;top:2652px;font-family:'Montserrat',sans-serif;font-weight:700;font-size:37px;color:var(--ink)}
.post{position:absolute;top:2720px;width:292px}
.post .pic{height:206px}
.post .date{margin-top:26px;font-family:'Montserrat',sans-serif;font-weight:500;font-size:15px;color:var(--teal)}
.post h5{margin-top:10px;font-family:'Montserrat',sans-serif;font-weight:700;font-size:19px;line-height:28px;color:var(--ink)}
.post p{margin-top:18px;font-size:14px;line-height:23px;color:#444}
.post a{display:inline-block;margin-top:18px;font-size:13px;color:#333;text-decoration:underline}

/* features + footer */
.footer-bg{position:absolute;left:0;top:3382px;width:1200px;height:707px;background:var(--black)}
.features{position:absolute;left:111px;top:3306px;width:977px;height:168px;background:var(--mint-soft);display:flex;align-items:center}
.feature{display:flex;align-items:center;gap:18px;font-family:'Montserrat',sans-serif;font-weight:700;font-size:16px;color:#3f3f3f;padding-left:32px}
.feature + .feature{border-left:1px solid #9fd8cf}
.newsletter h3{position:absolute;left:113px;top:3538px;font-family:'Montserrat',sans-serif;font-weight:700;font-size:27px;color:var(--white);letter-spacing:.5px}
.newsletter .field{position:absolute;left:549px;top:3533px;width:322px;height:45px;background:var(--white);font-size:13px;color:#777;padding:13px 15px}
.newsletter .go{position:absolute;left:882px;top:3533px;width:151px;height:45px;background:var(--teal);color:var(--white);font-family:'Montserrat',sans-serif;font-weight:500;font-size:16px;display:flex;align-items:center;justify-content:center}
.hr{position:absolute;left:111px;width:977px;height:1px;background:#3a3a3a}
.col{position:absolute;top:3681px;color:var(--white)}
.col h6{font-family:'Montserrat',sans-serif;font-weight:500;font-size:20px;letter-spacing:.5px;margin-bottom:26px}
.col li{list-style:none;font-size:14px;line-height:31px}
.col li::before{content:"›";margin-right:14px;color:#ccc}
.contact-row{display:flex;gap:18px;font-size:14px;line-height:20px;margin-bottom:14px}
.contact-row svg{flex:none;margin-top:2px}
.copyright{position:absolute;left:111px;top:4024px;font-size:15px;color:var(--white)}
.pay{position:absolute;top:4021px;width:40px;height:25px;border-radius:3px}
</style>
</head>
<body>

<header class="site-header">
  <div class="brand-name">Vek furniture</div>
  <nav class="main-nav"><span>HOME</span><span>ABOUT</span><span>OUR PRODUCTS</span><span>UPDATES</span><span>CONTACT</span></nav>
  <div class="nav-icons">
    <svg width="22" height="22" viewBox="0 0 22 22" fill="none" stroke="#fff" stroke-width="2"><circle cx="11" cy="7" r="5"/><path d="M2 21c1-5 5-7 9-7s8 2 9 7z"/></svg>
    <svg width="30" height="24" viewBox="0 0 30 24" fill="none" stroke="#fff" stroke-width="2"><path d="M1 3h5l3 13h14l3-9H8"/><circle cx="11" cy="21" r="2"/><circle cx="21" cy="21" r="2"/><circle cx="26" cy="4" r="3" fill="#fff"/></svg>
    <svg width="22" height="22" viewBox="0 0 22 22" fill="none" stroke="#fff" stroke-width="3"><circle cx="9" cy="9" r="6"/><path d="M14 14l6 6"/></svg>
  </div>
</header>

<section class="hero">
  <div class="big">VEK</div>
  <div class="hero-photo" role="img" aria-label="Blue velvet tufted arm chair on wooden legs"></div>
  <div class="kicker">FURNITURE</div>
  <h1>ARM CHAIR</h1>
  <a class="btn" style="left:114px;top:464px;width:146px;height:50px">SHOP NOW</a>
  <div class="hero-bump"></div>
  <div class="dots" style="left:566px;top:607px;gap:8px"><i class="on" style="width:16px;height:16px"></i><i style="width:8px;height:8px"></i><i style="width:8px;height:8px"></i><i style="width:8px;height:8px"></i></div>
</section>

<section class="category">
  <div class="section-ghost" style="top:835px;font-size:70px">COLLECTIONS</div>
  <div class="section-title" style="top:870px;font-size:36px">OUR CATEGORY</div>

  <div class="cat" style="left:111px;top:966px">
    <div class="frame"></div><div class="card"><div class="notch"></div><h3>BED</h3><a>VIEW MORE</a></div>
    <div class="pic" role="img" aria-label="Upholstered bed with navy bedding" style="left:10px;top:200px;width:322px;height:184px;background:linear-gradient(160deg,#b9ab98,#2d3f7a)"></div>
  </div>
  <div class="cat alt" style="left:446px;top:1001px">
    <div class="frame"></div><div class="card"><div class="notch"></div><h3>SOFA</h3><a>VIEW MORE</a></div>
    <div class="pic" role="img" aria-label="Dark grey three-seat sofa with red cushions" style="left:12px;top:220px;width:302px;height:152px;background:linear-gradient(180deg,#3d3f42,#232427)"></div>
  </div>
  <div class="cat" style="left:782px;top:966px">
    <div class="frame"></div><div class="card"><div class="notch"></div><h3>ARM CHAIR</h3><a>VIEW MORE</a></div>
    <div class="pic" role="img" aria-label="Yellow wingback arm chair" style="left:68px;top:128px;width:220px;height:280px;border-radius:80px 80px 30px 30px;background:radial-gradient(ellipse at 50% 40%,#f6d23a,#e4b810)"></div>
  </div>
</section>

<section class="products">
  <h2>Our Products</h2>
  <div class="rule"></div>
  <div class="tab" style="left:232px;width:206px">
    <svg width="40" height="30" viewBox="0 0 40 30" fill="none" stroke="currentColor" stroke-width="2"><rect x="3" y="3" width="34" height="18"/><rect x="8" y="7" width="10" height="6"/><rect x="22" y="7" width="10" height="6"/><path d="M1 21h38v5H1zM4 26v3M36 26v3"/></svg>BED</div>
  <div class="tab" style="left:449px;width:206px">
    <svg width="44" height="28" viewBox="0 0 44 28" fill="none" stroke="currentColor" stroke-width="2"><rect x="6" y="3" width="32" height="14"/><rect x="1" y="10" width="7" height="12"/><rect x="36" y="10" width="7" height="12"/><path d="M8 17h28v5M6 22v4M38 22v4"/></svg>SOFA</div>
  <div class="tab on" style="left:665px;width:302px">
    <svg width="36" height="40" viewBox="0 0 36 40" fill="none" stroke="currentColor" stroke-width="2"><rect x="6" y="2" width="24" height="24"/><rect x="1" y="14" width="6" height="16"/><rect x="29" y="14" width="6" height="16"/><path d="M7 24h22v6H7zM5 30v8M31 30v8"/></svg>ARM CHAIR</div>

  <div class="prod" style="left:111px">
    <div class="box"><div class="pic" role="img" aria-label="Light blue tufted arm chair" style="background:radial-gradient(ellipse at 50% 40%,#6bb8e0,#3a8fc0)"></div><div class="stars">★★★★★</div></div>
    <div class="price">$180,00</div><h4>Classic sofa &amp; arm chair</h4>
    <p>Sed ut perspiciatis unde omnis iste natus<br>error sit voluptatem accusantium</p>
    <a class="btn">SHOP NOW</a>
  </div>
  <div class="prod" style="left:449px">
    <div class="box"><div class="pic" role="img" aria-label="Rust orange lounge arm chair" style="background:radial-gradient(ellipse at 50% 40%,#c5603a,#9c4322)"></div><div class="stars">★★★★★</div></div>
    <div class="price">$180,00</div><h4>Classic sofa &amp; arm chair</h4>
    <p>Sed ut perspiciatis unde omnis iste natus<br>error sit voluptatem accusantium</p>
    <a class="btn">SHOP NOW</a>
  </div>
  <div class="prod" style="left:787px">
    <div class="box"><div class="pic" role="img" aria-label="Red tufted wingback arm chair" style="background:radial-gradient(ellipse at 50% 40%,#e2493f,#b8282a)"></div><div class="stars">★★★★★</div></div>
    <div class="price">$180,00</div><h4>Classic sofa &amp; arm chair</h4>
    <p>Sed ut perspiciatis unde omnis iste natus<br>error sit voluptatem accusantium</p>
    <a class="btn">SHOP NOW</a>
  </div>

  <div class="dots" style="left:548px;top:880px;gap:14px"><i class="on" style="width:28px;height:28px"></i><i style="width:15px;height:15px;background:var(--teal)"></i><i style="width:15px;height:15px;background:var(--teal)"></i><i style="width:15px;height:15px;background:var(--teal)"></i></div>
</section>

<section class="news">
  <h2 class="news-title">Latest News</h2>
  <article class="post" style="left:111px">
    <div class="pic" role="img" aria-label="Relaxed person stretching on a green sofa" style="background:linear-gradient(135deg,#d8c4a2,#7f8f78)"></div>
    <div class="date">MAR 25, 2023</div>
    <h5>Neque porro quisquam est qui dolorem ipsum quia</h5>
    <p>Nulla at diam ornare, aliquam urna vel, commodo urna. Nam id risus a est luctus consectetur quis eget libero.</p>
    <a>Learn More &gt;</a>
  </article>
  <article class="post" style="left:453px">
    <div class="pic" role="img" aria-label="Person sleeping on white pillows" style="background:linear-gradient(135deg,#f1ece8,#d9cfc8)"></div>
    <div class="date">MAR 25, 2023</div>
    <h5>Neque porro quisquam est qui dolorem ipsum quia</h5>
    <p>Nulla at diam ornare, aliquam urna vel, commodo urna. Nam id risus a est luctus consectetur quis eget libero.</p>
    <a>Learn More &gt;</a>
  </article>
  <article class="post" style="left:794px">
    <div class="pic" role="img" aria-label="Living room with green sofa, yellow throw and plants" style="background:linear-gradient(180deg,#ece8df,#4f6d5b 70%,#c9a76a)"></div>
    <div class="date">MAR 25, 2023</div>
    <h5>Neque porro quisquam est qui dolorem ipsum quia</h5>
    <p>Nulla at diam ornare, aliquam urna vel, commodo urna. Nam id risus a est luctus consectetur quis eget libero.</p>
    <a>Learn More &gt;</a>
  </article>
</section>

<div class="footer-bg"></div>

<section class="features">
  <div class="feature" style="width:322px">
    <svg width="58" height="74" viewBox="0 0 58 74" fill="none" stroke="#00AB8E" stroke-width="3"><circle cx="29" cy="28" r="22"/><circle cx="29" cy="28" r="14"/><path d="M29 21l2 5h5l-4 3 2 5-5-3-5 3 2-5-4-3h5z" fill="#00AB8E"/><path d="M15 46l-7 22 8-4 5 7 6-19M43 46l7 22-8-4-5 7-6-19"/></svg>
    HIGHEST QUALITY</div>
  <div class="feature" style="width:274px">
    <svg width="36" height="74" viewBox="0 0 36 74" fill="none" stroke="#00AB8E" stroke-width="3"><path d="M18 2v70M30 16c-4-5-24-6-24 6s24 8 24 22-22 12-26 6"/></svg>
    LOWEST PRICES</div>
  <div class="feature" style="width:380px">
    <svg width="68" height="68" viewBox="0 0 68 68" fill="none" stroke="#00AB8E" stroke-width="3"><circle cx="34" cy="34" r="31"/><path d="M34 12l18 7v14c0 12-9 20-18 23-9-3-18-11-18-23V19z"/><path d="M25 34l7 7 12-13"/></svg>
    SATISFACTION GUARANTEED</div>
</section>

<section class="newsletter">
  <h3>SIGN UP FOR NEWSLETTER</h3>
  <div class="field">Enter email</div>
  <div class="go">SUBSCRIPTION</div>
</section>
<div class="hr" style="top:3618px"></div>

<footer>
  <div class="col" style="left:110px">
    <h6>CONTACT US</h6>
    <div class="contact-row"><svg width="16" height="22" viewBox="0 0 16 22"><path d="M8 0a8 8 0 0 0-8 8c0 6 8 14 8 14s8-8 8-14a8 8 0 0 0-8-8z" fill="#00AB8E"/><circle cx="8" cy="8" r="3" fill="#000"/></svg><span style="font-size:13px">ADDRESS<br>48 Alder Row, Brookfield, UK</span></div>
    <div class="contact-row"><svg width="18" height="18" viewBox="0 0 18 18"><path d="M4 1l4 4-2 3c1 2 3 4 5 5l3-2 4 4-3 3C8 18 0 10 1 4z" fill="#00AB8E"/></svg><span>Phone: (014) 382-5591</span></div>
    <div class="contact-row"><svg width="18" height="14" viewBox="0 0 18 14"><rect width="18" height="14" fill="#00AB8E"/><path d="M0 0l9 7 9-7" stroke="#000" stroke-width="1.5" fill="none"/></svg><span>E-mail: hello@vekhome.test</span></div>
    <div class="contact-row"><svg width="18" height="18" viewBox="0 0 18 18"><circle cx="9" cy="9" r="9" fill="#00AB8E"/><path d="M9 4v5h4" stroke="#000" stroke-width="2" fill="none"/></svg><span>Opening hours:<br><span style="font-size:13px;line-height:24px">Man–Thurs: 10.00–18.30<br>Fri: 10.30–14.00</span></span></div>
  </div>
  <div class="col" style="left:448px">
    <h6>FAVORITES</h6>
    <ul><li>Lorem ipsum dolor</li><li>Vestibulum</li><li>Suspendisse iaculis</li><li>Integer feugiat</li><li>Donec at neque</li></ul>
  </div>
  <div class="col" style="left:669px">
    <h6>CUSTOMER SERVICE</h6>
    <ul><li>Contact Us</li><li>Shopping Cart</li><li>Wishlist</li><li>FAQ</li><li>Shipping Policy</li></ul>
  </div>
  <div class="col" style="left:927px">
    <h6>MY ACCOUNT</h6>
    <ul><li>Sign In</li><li>View Cart</li><li>Wishlist</li><li>FAQ</li></ul>
  </div>
  <div class="hr" style="top:3982px"></div>
  <div class="copyright">Vek Furniture© 2023. All Rights Reserved.</div>
  <div class="pay" style="left:939px;background:#e6e6ee"></div>
  <div class="pay" style="left:992px;background:#5a9ed6"></div>
  <div class="pay" style="left:1048px;background:#e8e8e8"></div>
</footer>

</body>
</html>
```